Graphic Design of Business Process

We require an eye-catching, sophisticated design of 2 business processes (attached), that will be used digitally AND for print (to be put on walls in our office).

The basic layout is attached. We require a creative, professional designer to re-design these so that they look appealing but still able to grasp all the information.

We will require vector files and editable project files for final delivery. You may refer to our website (lanternwickhub.com.au) for an indication of our brand.

If you have any questions, please ask.

Thank you.

```html
<!DOCTYPE html>
<html lang="en">
<head>
<meta charset="utf-8">
<title>Sales Content Funnel</title>
<link rel="stylesheet" href="https://fonts.googleapis.com/css2?family=Titillium+Web:wght@700;900&family=Source+Sans+3:wght@700&family=Poppins:wght@800&family=Comfortaa:wght@300&display=swap">
<style>
  :root {
    --band-blue: #29abd6;
    --band-blue-deep: #2f8fc3;
    --red: #ec5050;
    --orange: #f9a51b;
    --green: #4cae55;
    --teal: #2bbad6;
    --purple: #7f5ea8;
    --brown: #8c4a1c;
    --deep-green: #1d5a2c;
    --deep-blue: #17607f;
    --hero: #f4b41a;
    --hub: #3db049;
    --hygiene: #29a8d8;
    --ink: #111;
  }
  * { margin: 0; padding: 0; box-sizing: border-box; }
  html, body { width: 958px; height: 1200px; overflow: hidden; background: #fff; }
  .canvas { position: relative; width: 958px; height: 1200px; }
  .top-band { position: absolute; left: 0; top: 0; width: 958px; height: 50px; background: var(--band-blue); }
  .bottom-band { position: absolute; left: 0; top: 1144px; width: 958px; height: 56px;
    background: linear-gradient(var(--band-blue) 0 20px, var(--band-blue-deep) 20px); }
  .diagram { position: absolute; left: 0; top: 0; }
  .head { font-family: "Titillium Web", sans-serif; font-weight: 700; text-anchor: middle; }
  .body { font-family: "Source Sans 3", sans-serif; font-weight: 700; text-anchor: middle; }
  .body-left { font-family: "Source Sans 3", sans-serif; font-weight: 700; text-anchor: start; }
  .ul { text-decoration: underline; }
  .legend-title { font-family: "Poppins", sans-serif; font-weight: 800; }
  .legend-sub { font-family: "Comfortaa", sans-serif; font-weight: 300; }
</style>
</head>
<body>
<div class="canvas">
  <div class="top-band"></div>

  <svg class="diagram" width="958" height="1200" viewBox="0 0 958 1200">
    <defs>
      <marker id="arrowhead" viewBox="0 0 10 10" refX="8" refY="5" markerWidth="22" markerHeight="22" markerUnits="userSpaceOnUse" orient="auto">
        <path d="M0 0 L10 5 L0 10 Z" fill="var(--ink)"/>
      </marker>
    </defs>

    <g class="funnel">
      <polygon points="44,172 696,172 633,294 105,294" fill="var(--red)"/>
      <polygon points="105,294 633,294 572,414 165,414" fill="var(--orange)"/>
      <polygon points="165,414 572,414 510,534 224,534" fill="var(--green)"/>
      <polygon points="224,534 510,534 444,662 288,662" fill="var(--teal)"/>
      <polygon points="44,172 88,172 320,662 288,662" fill="#fff" opacity="0.3"/>
      <polygon points="580,172 696,172 444,662 410,662" fill="#000" opacity="0.06"/>
    </g>

    <text class="head" x="378" y="248" font-size="84" fill="#fff">SALES</text>
    <text class="head" x="378" y="284" font-size="27.5" fill="#fff">Content Funnel</text>

    <text class="head" x="375" y="339" font-size="49" fill="#fff">AWARENESS</text>
    <text class="body" x="375" y="357" font-size="18.5" fill="var(--brown)">IDENTIFY PROBLEM/NEED</text>
    <text class="body" x="375" y="377" font-size="17.5" fill="#fff">• Aspirational</text>
    <text class="body" x="372" y="402" font-size="19" fill="#fff">• Market The <tspan class="ul">Outcome</tspan> Not Product</text>

    <text class="head" x="372" y="446" font-size="35.5" fill="#fff">CONSIDERATION</text>
    <text class="body" x="372" y="466" font-size="18.5" fill="var(--deep-green)">EVALUATE ALTERNATIVES</text>
    <text class="body" x="372" y="487" font-size="17.5" fill="#fff">•Why is <tspan class="ul">this solution</tspan> better than others</text>
    <text class="body" x="374" y="508" font-size="17.5" fill="#fff">• <tspan class="ul">How</tspan> is the provider going to solve</text>
    <text class="body" x="376" y="525" font-size="17.5" fill="#fff">my need</text>

    <text class="head" x="370" y="561" font-size="22" fill="#fff">ACTION/DECISION</text>
    <text class="body" x="370" y="580" font-size="15.5" fill="var(--deep-blue)">PRESENT AN OFFER</text>
    <text class="body" x="366" y="605" font-size="17.5" fill="#fff">• <tspan class="ul">Which</tspan> Provider?</text>

    <g class="connectors" fill="none" stroke="var(--ink)" stroke-width="7" stroke-linecap="round">
      <path d="M810,490 C930,470 935,372 866,362" marker-end="url(#arrowhead)"/>
      <path d="M770,596 C872,596 872,500 808,484" marker-end="url(#arrowhead)"/>
      <path d="M660,662 C760,660 796,652 796,626 C796,604 780,598 758,596" marker-end="url(#arrowhead)"/>
      <path d="M490,662 L452,662" marker-end="url(#arrowhead)"/>
    </g>

    <polygon class="tag-problem" points="654,306 874,306 828,402 612,402" fill="var(--orange)"/>
    <text class="body" x="752" y="336" font-size="23" fill="var(--brown)">Problem &amp; Solution</text>
    <text class="body" x="724" y="361" font-size="20" fill="#fff">• Subject Showing</text>
    <text class="body" x="732" y="381" font-size="20" fill="#fff">Symptons of Problems</text>

    <polygon class="tag-providers" points="590,441 810,441 768,532 552,532" fill="var(--green)"/>
    <text class="body" x="693" y="463" font-size="22" fill="var(--deep-green)">Providers &amp; Types of</text>
    <text class="body" x="693" y="482" font-size="22" fill="var(--deep-green)">Solution</text>
    <text class="body-left" x="572" y="506" font-size="20" fill="#fff">•Subject Gives</text>
    <text class="body-left" x="565" y="525" font-size="20" fill="#fff">Name to Problem</text>

    <polygon class="tag-convert" points="526,574 750,574 732,616 512,616" fill="var(--teal)"/>
    <text class="body" x="631" y="602" font-size="24" fill="var(--deep-blue)">Convert &amp; Retain</text>

    <polygon class="tag-referral" points="490,652 664,652 654,685 480,685" fill="var(--purple)"/>
    <text class="body" x="571" y="675" font-size="19" fill="#fff">Wom &amp; Referral</text>

    <g class="legend">
      <rect x="38" y="770" width="58" height="108" fill="var(--hero)"/>
      <rect x="96" y="876" width="469" height="3" fill="var(--hero)"/>
      <text class="legend-title" x="118" y="822" font-size="62" fill="var(--hero)">Hero</text>
      <text class="legend-sub" x="117" y="866" font-size="35" fill="var(--hero)">Tentpole Campaigns</text>

      <rect x="38" y="893" width="58" height="108" fill="var(--hub)"/>
      <rect x="96" y="999" width="469" height="3" fill="var(--hub)"/>
      <text class="legend-title" x="118" y="944" font-size="62" fill="var(--hub)">Hub</text>
      <text class="legend-sub" x="117" y="988" font-size="35" fill="var(--hub)">Regular “Push” Content</text>

      <rect x="38" y="1014" width="58" height="110" fill="var(--hygiene)"/>
      <rect x="96" y="1122" width="469" height="3" fill="var(--hygiene)"/>
      <text class="legend-title" x="118" y="1066" font-size="62" fill="var(--hygiene)">Hygiene</text>
      <text class="legend-sub" x="117" y="1110" font-size="35" fill="var(--hygiene)">Always-on “Pull” Content</text>
    </g>
  </svg>

  <div class="bottom-band"></div>
</div>
</body>
</html>
```